A modern web page for a software product

We need a web page for a software product, which is an advanced solution based on Machine Learning and Natural Language processing. We already have a logo of the product and expect the web page to be inline with the logo colors. The design should be for one page web site with scrolled sections - details of the content and guidelines in the attachments.

Target Market(s)

software company

Industry/Entity Type

It Company

Number of Pages Required

1 page

Colors

Designer to choose colors to be used in the design.

Requirements
Must have
• - modern icons and graphics
• - inline with the logo colors
• - be related to Machine Learining, AI, data processing
• - should have two language versions: english and polish both are attached.
Nice to have
• - animation/motion
Should not have
• - any photos embedded

```html
<!DOCTYPE html>
<html lang="en">
<head>
<meta charset="utf-8">
<title>NEXL — Personal Data Discovery</title>
<link rel="stylesheet" href="https://fonts.googleapis.com/css2?family=Open+Sans:wght@400;600;700&family=Montserrat:wght@600;700&display=swap">
<style>
:root{
  --navy:#1c2733;
  --navy-2:#243240;
  --teal:#1b95ad;
  --teal-dark:#0f6f8a;
  --teal-deep:#0b4f6a;
  --box:#0d5f7c;
  --box-edge:#3cb7cf;
  --white:#ffffff;
  --ink:#2a3440;
  --muted:#6d7985;
  --paper:#f3f5f7;
  --footer:#3b4148;
}
*{box-sizing:border-box;margin:0;padding:0}
html,body{width:882px;height:1200px;overflow:hidden;background:var(--white);font-family:"Open Sans",Arial,sans-serif;color:var(--ink)}
.page{position:relative;width:882px;height:1200px}

/* header */
.brand{position:absolute;left:16px;top:10px;font-family:"Montserrat",Arial,sans-serif;font-weight:700;font-size:26px;color:var(--teal-dark);letter-spacing:1px}
.nav{position:absolute;left:245px;top:0;width:637px;height:50px;background:var(--navy);display:flex}
.nav a{flex:1;display:flex;align-items:center;justify-content:center;text-align:center;color:var(--white);font-size:9.5px;font-weight:700;text-transform:uppercase;text-decoration:none;line-height:1.3;padding:0 10px;border-right:1px solid #34414f}
.nav a.active{background:var(--teal-dark)}
.dropdown{position:absolute;left:245px;top:50px;width:190px;background:var(--navy-2);padding:6px 0;z-index:3}
.dropdown a{display:block;color:#dfe6ec;font-size:8.5px;text-decoration:none;padding:5px 12px;border-bottom:1px solid #34414f}
.dropdown a:first-child{background:var(--teal-dark);color:var(--white);font-weight:700}

/* hero */
.hero{position:absolute;left:0;top:70px;width:882px;height:490px;background:linear-gradient(160deg,var(--teal) 0%,var(--teal-dark) 55%,var(--teal-deep) 100%)}
.hero-panel{position:absolute;left:60px;top:20px;width:762px;height:450px;background:rgba(8,50,70,.25);border:1px solid rgba(255,255,255,.12)}
.feature{position:absolute;background:var(--box);border:1px solid var(--box-edge);display:flex;align-items:center;gap:12px;padding:10px 14px;color:var(--white)}
.feature svg{flex:none}
.feature h3{font-size:9.5px;font-weight:700;text-transform:uppercase;line-height:1.35}
.feature ul{list-style:none;margin-top:5px}
.feature li{font-size:8.5px;line-height:1.5;color:#d6eef4}
.feature li::before{content:"– "}

/* capabilities */
.capabilities{position:absolute;left:0;top:600px;width:882px;height:280px;background:linear-gradient(180deg,var(--navy) 0%,#222f3c 100%)}
.cap{position:absolute;width:210px;text-align:center;color:var(--white)}
.cap svg{display:block;margin:0 auto 8px}
.cap h4{font-size:9.5px;font-weight:700;text-transform:uppercase;line-height:1.35}

/* details */
.details{position:absolute;left:0;top:880px;width:882px;height:255px;background:var(--paper)}
.detail-head{position:absolute;height:26px;background:var(--navy);color:var(--white);font-size:9px;font-weight:700;text-transform:uppercase;display:flex;align-items:center;gap:8px;padding-left:6px}
.detail-head .dot{width:16px;height:16px;border-radius:50%;background:var(--teal);flex:none}
.detail-list{position:absolute;list-style:none}
.detail-list li{font-size:8.5px;line-height:1.6;color:var(--ink);padding-left:12px;position:relative;text-transform:uppercase}
.detail-list li::before{content:"";position:absolute;left:0;top:5px;width:5px;height:5px;background:var(--teal)}

/* footer */
.contact-bar{position:absolute;left:0;top:1142px;width:882px;height:32px;background:var(--footer);display:flex}
.contact-bar span{flex:1;display:flex;align-items:center;justify-content:center;gap:6px;color:var(--white);font-size:8.5px;border-right:1px solid #555c64}
.contact-bar svg{flex:none}
.copyright{position:absolute;left:0;top:1182px;width:882px;text-align:center;font-size:8px;color:var(--muted)}
</style>
</head>
<body>
<div class="page">

  <header>
    <div class="brand">NEXL</div>
    <nav class="nav">
      <a class="active" href="#">Discovery and classification<br>of personal data</a>
      <a href="#">Consents management<br>support</a>
      <a href="#">Linked registry<br>of all personal data</a>
      <a href="#">Supports structured and unstructured<br>data sources</a>
    </nav>
    <div class="dropdown">
      <a href="#">Polish personal data detection</a>
      <a href="#">Financial and currency data detection</a>
      <a href="#">Sensitive data flags for review</a>
    </div>
  </header>

  <section class="hero">
    <div class="hero-panel"></div>

    <div class="feature" style="left:90px;top:100px;width:350px;height:110px">
      <svg width="34" height="34" viewBox="0 0 34 34" fill="none" stroke="#fff" stroke-width="1.6"><circle cx="14" cy="14" r="9"/><line x1="21" y1="21" x2="30" y2="30"/></svg>
      <div>
        <h3>Detection of personal and sensitive data for GDPR compliance</h3>
        <ul>
          <li>Detects personal data in files</li>
          <li>Classifies documents, emails, logs and databases</li>
          <li>Flags sensitive records for review and masking</li>
        </ul>
      </div>
    </div>

    <div class="feature" style="left:470px;top:125px;width:320px;height:56px">
      <svg width="30" height="30" viewBox="0 0 30 30" fill="none" stroke="#fff" stroke-width="1.6"><rect x="4" y="5" width="22" height="20"/><line x1="4" y1="12" x2="26" y2="12"/><line x1="4" y1="18" x2="26" y2="18"/></svg>
      <h3>Fast cataloging and classification of data and sources</h3>
    </div>

    <div class="feature" style="left:90px;top:232px;width:350px;height:56px">
      <svg width="30" height="30" viewBox="0 0 30 30" fill="none" stroke="#fff" stroke-width="1.6"><circle cx="8" cy="15" r="4"/><circle cx="22" cy="8" r="4"/><circle cx="22" cy="22" r="4"/><line x1="11" y1="13" x2="19" y2="9"/><line x1="11" y1="17" x2="19" y2="21"/></svg>
      <h3>Linked data registry for GDPR compliance purposes</h3>
    </div>

    <div class="feature" style="left:470px;top:232px;width:320px;height:56px">
      <svg width="30" height="30" viewBox="0 0 30 30" fill="none" stroke="#fff" stroke-width="1.6"><rect x="6" y="13" width="18" height="13"/><path d="M10 13V9a5 5 0 0 1 10 0v4"/></svg>
      <h3>Management of consents and data access policies</h3>
    </div>

    <div class="feature" style="left:90px;top:310px;width:350px;height:56px">
      <svg width="30" height="30" viewBox="0 0 30 30" fill="none" stroke="#fff" stroke-width="1.6"><line x1="5" y1="26" x2="26" y2="26"/><rect x="7" y="16" width="4" height="10"/><rect x="14" y="10" width="4" height="16"/><rect x="21" y="5" width="4" height="21"/></svg>
      <h3>Customizable analytics and reporting</h3>
    </div>

    <div class="feature" style="left:470px;top:310px;width:320px;height:56px">
      <svg width="30" height="30" viewBox="0 0 30 30" fill="none" stroke="#fff" stroke-width="1.6"><rect x="4" y="4" width="9" height="9"/><rect x="17" y="17" width="9" height="9"/><path d="M13 8h8v9"/></svg>
      <h3>Ability to integrate with existing tools and data warehouses</h3>
    </div>

    <div class="feature" style="left:270px;top:392px;width:340px;height:56px">
      <svg width="30" height="30" viewBox="0 0 30 30" fill="none" stroke="#fff" stroke-width="1.6"><polyline points="10,8 3,15 10,22"/><polyline points="20,8 27,15 20,22"/><line x1="17" y1="6" x2="13" y2="24"/></svg>
      <h3>RESTful API for system management and integration</h3>
    </div>
  </section>

  <section class="capabilities">
    <div class="cap" style="left:65px;top:28px">
      <svg width="56" height="56" viewBox="0 0 56 56" fill="none" stroke="#fff" stroke-width="1.6"><circle cx="28" cy="28" r="26" stroke="#3cb7cf"/><rect x="17" y="16" width="22" height="24"/><line x1="21" y1="23" x2="35" y2="23"/><line x1="21" y1="29" x2="35" y2="29"/><line x1="21" y1="35" x2="30" y2="35"/></svg>
      <h4>Internal audits and verification of the current status in preparation for ensuring GDPR compliance</h4>
    </div>
    <div class="cap" style="left:336px;top:28px">
      <svg width="56" height="56" viewBox="0 0 56 56" fill="none" stroke="#fff" stroke-width="1.6"><circle cx="28" cy="28" r="26" stroke="#3cb7cf"/><ellipse cx="28" cy="18" rx="11" ry="4"/><path d="M17 18v20c0 2 5 4 11 4s11-2 11-4V18"/><path d="M17 28c0 2 5 4 11 4s11-2 11-4"/></svg>
      <h4>Cataloging sources that store sensitive data</h4>
    </div>
    <div class="cap" style="left:607px;top:28px">
      <svg width="56" height="56" viewBox="0 0 56 56" fill="none" stroke="#fff" stroke-width="1.6"><circle cx="28" cy="28" r="26" stroke="#3cb7cf"/><circle cx="25" cy="25" r="9"/><line x1="31" y1="31" x2="39" y2="39"/></svg>
      <h4>Defining the registry of personal data to implement rights to information, forgetfulness, data transfer</h4>
    </div>
    <div class="cap" style="left:65px;top:160px">
      <svg width="56" height="56" viewBox="0 0 56 56" fill="none" stroke="#fff" stroke-width="1.6"><circle cx="28" cy="28" r="26" stroke="#3cb7cf"/><path d="M18 28a10 10 0 0 1 18-6"/><polyline points="36,16 36,22 30,22"/><path d="M38 28a10 10 0 0 1-18 6"/><polyline points="20,40 20,34 26,34"/></svg>
      <h4>Continuous monitoring and classification of data</h4>
    </div>
    <div class="cap" style="left:336px;top:160px">
      <svg width="56" height="56" viewBox="0 0 56 56" fill="none" stroke="#fff" stroke-width="1.6"><circle cx="28" cy="28" r="26" stroke="#3cb7cf"/><circle cx="28" cy="28" r="10"/><line x1="28" y1="14" x2="28" y2="18"/><line x1="28" y1="38" x2="28" y2="42"/><line x1="14" y1="28" x2="18" y2="28"/><line x1="38" y1="28" x2="42" y2="28"/></svg>
      <h4>Use collected data to create additional business value</h4>
    </div>
    <div class="cap" style="left:607px;top:160px">
      <svg width="56" height="56" viewBox="0 0 56 56" fill="none" stroke="#fff" stroke-width="1.6"><circle cx="28" cy="28" r="26" stroke="#3cb7cf"/><rect x="16" y="18" width="10" height="8"/><rect x="30" y="18" width="10" height="8"/><rect x="16" y="30" width="10" height="8"/><rect x="30" y="30" width="10" height="8"/></svg>
      <h4>Classification of documents</h4>
    </div>
  </section>

  <section class="details">
    <div class="detail-head" style="left:40px;top:22px;width:390px"><span class="dot"></span>Ready for detection of Polish personal data</div>
    <div class="detail-head" style="left:452px;top:22px;width:390px"><span class="dot"></span>Non-personal data detection (also "dirty" types of currencies)</div>
    <ul class="detail-list" style="left:52px;top:56px;width:370px">
      <li>Names, addresses, IDs</li>
      <li>Bank account numbers</li>
      <li>Contact details in free text</li>
      <li>Custom rules for extended detection</li>
    </ul>
    <ul class="detail-list" style="left:464px;top:56px;width:370px">
      <li>National language processing</li>
      <li>Machine learning</li>
      <li>Currency and amounts</li>
      <li>Custom models for data detection specific to your organization</li>
    </ul>
    <div class="detail-head" style="left:40px;top:132px;width:390px"><span class="dot"></span>Supports structured and unstructured data sources</div>
    <div class="detail-head" style="left:452px;top:132px;width:390px"><span class="dot"></span>Ready for high performance processing</div>
    <ul class="detail-list" style="left:52px;top:166px;width:370px">
      <li>Shared storage and drives, content management and servers, file servers</li>
      <li>Relational databases, data lakes, archives</li>
      <li>Relational databases</li>
      <li>NoSQL databases</li>
      <li>Data streams</li>
    </ul>
    <ul class="detail-list" style="left:464px;top:166px;width:370px">
      <li>Shared storage and drives, content management and servers, file servers</li>
      <li>Relational databases, data lakes, archives</li>
      <li>Distributed processing</li>
    </ul>
  </section>

  <footer>
    <div class="contact-bar">
      <span><svg width="12" height="12" viewBox="0 0 12 12" fill="none" stroke="#fff"><circle cx="6" cy="6" r="5"/><line x1="1" y1="6" x2="11" y2="6"/></svg>www.nexl-data.example</span>
      <span><svg width="10" height="12" viewBox="0 0 10 12" fill="none" stroke="#fff"><path d="M5 11C2 7 1 5.5 1 4a4 4 0 0 1 8 0c0 1.5-1 3-4 7z"/></svg>ul. Przykładowa 1, Warszawa</span>
      <span><svg width="12" height="12" viewBox="0 0 12 12" fill="none" stroke="#fff"><path d="M2 1h3l1 3-2 1a7 7 0 0 0 3 3l1-2 3 1v3c-6 0-10-4-9-9z"/></svg>+48 000 000 000</span>
      <span><svg width="12" height="10" viewBox="0 0 12 10" fill="none" stroke="#fff"><rect x="0.5" y="0.5" width="11" height="9"/><polyline points="1,1 6,6 11,1"/></svg>hello@nexl-data.example</span>
    </div>
    <p class="copyright">© NEXL. All rights reserved.</p>
  </footer>

</div>
</body>
</html>
```